Modern Label for cleaning products for the brand Dorvalix

We need a label design for our line of cleaning products. The label should feature our logo and an image to identify the product's intended use. I've added our logo and an image for use. This only concerns the design of the label on the front of the bottle.

Label dimensions:
Label 1 (500ml bottle with spray): width 58mm x height 115mm
Label 2: (1L bottle): width 73mm x height 140mm
The design must be consistent for both bottles which you find in the pictures.

The bottles to be labeled are white. See the attachment for a photo of the bottles.

The photo must also appear on the label to identify the product's intended use.

Product information:
Brand: Dorvalix
Product: Sanitary Cleaner

This text must be placed on the label:
"Cleans, descales & freshens. followed with this text: "Ideal for quick and powerful cleaning. A ready-to-use product for everyday use."

- Mention the seperate USP's: Sanitary, Bathroom, Toilet, Wet areas

Appearance: This is a consumer product, but it must have a professional appearance. We would like to see a design that use the color blue from our logo.

Target Market(s)

Consumers who take care of their homes and want to maintain it the correct (professional) way

Font styles to use
Sans Serif

Colors
0054AA
0677BA
7BADD7
CADEEF
E8F1F8

Requirements
Must have
• USP's + use of image and logo + blend in 1 design
Nice to have
• Keep the color of the logo in the design
Should not have
• Comic sans

```html
<!DOCTYPE html>
<html lang="en">
<head>
<meta charset="utf-8">
<title>Dorvalix Sanitary Cleaner – 1L Label</title>
<link href="https://fonts.googleapis.com/css2?family=Poppins:wght@300;400;500;700&display=swap" rel="stylesheet">
<style>
  :root {
    --brand-blue: #0054AA;
    --mid-blue: #0677BA;
    --soft-blue: #5a8fca;
    --icon-blue: #3f7cc4;
    --pale-blue: #CADEEF;
    --mist-blue: #E8F1F8;
    --ink: #4a4a48;
    --body-ink: #333333;
    --rule: #9a9a9a;
    --page: #eef1f4;
    --label: #ffffff;
  }
  * { margin: 0; padding: 0; box-sizing: border-box; }
  html, body {
    width: 1200px; height: 1117px; overflow: hidden;
    background: var(--page);
    font-family: "Poppins", sans-serif;
  }
  .label {
    position: absolute; left: 330px; top: 38px;
    width: 540px; height: 1040px;
    background: var(--label);
    overflow: hidden;
    box-shadow: 0 2px 14px rgba(0,0,0,0.08);
  }
  .brand {
    position: absolute; left: 31px; top: 28px;
    display: flex; align-items: center; gap: 24px;
  }
  .brand-dot {
    width: 82px; height: 82px; border-radius: 50%;
    background: var(--mid-blue);
  }
  .brand-name {
    font-weight: 700; font-size: 50px; color: var(--ink);
    letter-spacing: -0.5px; line-height: 1;
  }
  .product-name {
    position: absolute; left: 27px; top: 128px;
    font-weight: 300; font-size: 86px; line-height: 72px;
    color: var(--ink); letter-spacing: -1px;
  }
  .usage-photo {
    position: absolute; left: 0; top: 280px;
    width: 540px; height: 416px;
  }
  .claim {
    position: absolute; left: 27px; top: 722px;
    font-weight: 500; font-size: 29px; color: var(--soft-blue);
    letter-spacing: -0.6px;
  }
  .description {
    position: absolute; left: 27px; top: 777px;
    font-size: 20.5px; line-height: 22px; color: var(--body-ink);
    font-weight: 400;
  }
  .rule {
    position: absolute; left: 27px; width: 498px; height: 1px;
    background: var(--rule);
  }
  .rule--top { top: 845px; }
  .rule--bottom { top: 948px; }
  .uses {
    position: absolute; left: 27px; top: 876px; width: 498px;
    display: flex; justify-content: space-between; align-items: center;
  }
  .use {
    display: flex; align-items: center; gap: 7px;
    font-size: 14.5px; color: #555; font-weight: 400;
  }
  .use svg { width: 36px; height: 36px; }
  .volume {
    position: absolute; left: 0; width: 540px; top: 982px;
    text-align: center; font-size: 24px; color: var(--ink); font-weight: 300;
  }
</style>
</head>
<body>
  <div class="label">
    <div class="brand">
      <div class="brand-dot"></div>
      <span class="brand-name">dorvalix</span>
    </div>

    <h1 class="product-name">SANITARY<br>CLEANER</h1>

    <svg class="usage-photo" viewBox="0 0 540 416" role="img" aria-label="Photograph of a bright modern bathroom with a glass shower, washbasin, tiled bathtub and towel radiator, shown in soft greyscale">
      <defs>
        <linearGradient id="bathroomTone" x1="0" y1="0" x2="0" y2="1">
          <stop offset="0" stop-color="#e9e9e9"/>
          <stop offset="0.45" stop-color="#d2d2d2"/>
          <stop offset="0.75" stop-color="#b9b9b9"/>
          <stop offset="1" stop-color="#c7c7c7"/>
        </linearGradient>
      </defs>
      <path d="M0 92 C120 40 260 20 400 18 C470 17 510 10 540 0 L540 416 L0 416 Z" fill="url(#bathroomTone)"/>
      <path d="M0 92 C130 45 250 28 400 24 C470 22 510 15 540 6" fill="none" stroke="#ffffff" stroke-width="10" opacity="0.6"/>
    </svg>

    <p class="claim">Cleans, Descales &amp; Freshens</p>
    <p class="description">Ideal For Quick And Powerful Cleaning.<br>A Ready-To-Use Product For Everyday Use.</p>

    <div class="rule rule--top"></div>

    <div class="uses">
      <div class="use">
        <svg viewBox="0 0 36 36" fill="none" stroke="var(--icon-blue)" stroke-width="1.6" stroke-linecap="round" stroke-linejoin="round">
          <rect x="17" y="11" width="13" height="20" rx="2"/>
          <path d="M20 11V7h7v4M23 7V4h4"/>
          <path d="M3 29l6-5h8l4 3-4 3H9"/>
          <circle cx="9" cy="14" r="2"/><circle cx="12" cy="9" r="1.3"/>
        </svg>
        <span>Sanitary</span>
      </div>
      <div class="use">
        <svg viewBox="0 0 36 36" fill="none" stroke="var(--icon-blue)" stroke-width="1.6" stroke-linecap="round" stroke-linejoin="round">
          <path d="M3 15h30M5 15l2 9a4 4 0 0 0 4 3h14a4 4 0 0 0 4-3l2-9"/>
          <path d="M11 27l-2 4M25 27l2 4"/>
          <path d="M8 15V8a3 3 0 0 1 6 0"/>
        </svg>
        <span>Bathroom</span>
      </div>
      <div class="use">
        <svg viewBox="0 0 36 36" fill="none" stroke="var(--icon-blue)" stroke-width="1.6" stroke-linecap="round" stroke-linejoin="round">
          <path d="M4 8l18-3 2 24-18 3z"/>
          <path d="M10 27v-9M13 27V14M16 27V15M19 27v-8"/>
          <path d="M28 12h5M28 17h6M28 22h5"/>
        </svg>
        <span>Wet Areas</span>
      </div>
      <div class="use">
        <svg viewBox="0 0 36 36" fill="none" stroke="var(--icon-blue)" stroke-width="1.6" stroke-linecap="round" stroke-linejoin="round">
          <ellipse cx="27" cy="15" rx="6" ry="8"/>
          <ellipse cx="27" cy="15" rx="2" ry="3"/>
          <path d="M27 7H8a6 8 0 0 0 0 16h19"/>
          <path d="M8 23v5h12"/>
        </svg>
        <span>Toilet</span>
      </div>
    </div>

    <div class="rule rule--bottom"></div>

    <p class="volume">1L</p>
  </div>
</body>
</html>
```